Wedding Ceremony Equipment Hire Business Card

I need a business card design for a new business I created called Vow Outfitters. We hire out Wedding Ceremony equipment and decorations mainly for beach and garden wedding ceremonies that include delivery, set up and dismantle. We do offer DIY Chair Hire as well.
I'd like to have a similar design and colours to our website:
www.vowoutfitters-example.com.au
If possible would like the front to incorporate our information and logo and the back to have two faded example pictures of our wedding ceremonies.
I have attached two photos and our logo. Please let me know if you need a better pic of our logo though.

Target Market(s)

Newly engaged couples, aged 25 and upwards

Industry/Entity Type

Wedding

Contact Information for Business Card

Vow Outfitters
Merel Thorpe
0491 870 264
vowoutfitters@mailbox-example.com
www.social-example.com/VowOutfitters

```html
<!DOCTYPE html>
<html lang="en">
<head>
<meta charset="utf-8">
<title>Vow Outfitters – Business Card</title>
<link rel="stylesheet" href="https://fonts.googleapis.com/css2?family=Cinzel:wght@400;500&family=Pinyon+Script&display=swap">
<style>
  :root {
    --page: #ffffff;
    --sky-top: #2f5fae;
    --sky-low: #6f9fd8;
    --sea: #3c9aa6;
    --sand-light: #d9ab72;
    --sand-deep: #b98445;
    --harbour-sky: #9cc4e6;
    --harbour-city: #8a9aa5;
    --lawn-light: #4f7a3a;
    --lawn-dark: #1f3a1c;
    --mint-band: rgba(160, 215, 195, 0.72);
    --ink: #151515;
    --ink-soft: #2b2b2b;
    --white: #ffffff;
  }
  * { box-sizing: border-box; margin: 0; padding: 0; }
  html, body {
    width: 1200px; height: 900px; overflow: hidden;
    background: var(--page);
  }
  .canvas { position: relative; width: 1200px; height: 900px; }

  .card {
    position: absolute;
    width: 560px; height: 350px;
    border-radius: 22px;
    overflow: hidden;
  }
  .card--front { left: 560px; top: 100px; }
  .card--back  { left: 100px; top: 470px; }

  .photo { position: absolute; inset: 0; }
  .photo--beach {
    background: linear-gradient(180deg,
      var(--sky-top) 0%, var(--sky-low) 42%, var(--sea) 50%,
      var(--sand-light) 56%, var(--sand-deep) 100%);
  }
  .photo--garden {
    background: linear-gradient(180deg,
      var(--harbour-sky) 0%, var(--harbour-city) 24%,
      var(--lawn-light) 40%, var(--lawn-dark) 100%);
  }

  .brand {
    position: absolute;
    font-family: "Cinzel", serif;
    font-weight: 400;
    letter-spacing: 0.04em;
    white-space: nowrap;
  }
  .card--front .brand {
    left: 210px; top: 62px;
    font-size: 38px;
    color: var(--white);
  }

  .contact {
    position: absolute;
    left: 180px; top: 220px; width: 330px;
    text-align: center;
    color: var(--ink);
  }
  .contact__name {
    font-family: "Pinyon Script", cursive;
    font-size: 34px;
    line-height: 1;
    margin-bottom: 6px;
  }
  .contact__line {
    font-family: "Cinzel", serif;
    font-size: 12.5px;
    line-height: 1.45;
    letter-spacing: 0.06em;
    text-transform: uppercase;
    color: var(--ink-soft);
  }

  .band {
    position: absolute;
    left: 0; right: 0; top: 110px; height: 110px;
    background: var(--mint-band);
  }
  .card--back .brand {
    left: 0; right: 0; top: 143px;
    text-align: center;
    font-size: 38px;
    color: var(--ink);
  }
</style>
</head>
<body>
<main class="canvas">

  <section class="card card--front" aria-label="Business card front">
    <div class="photo photo--beach" role="img" aria-label="Photo of a beach wedding ceremony: rows of white folding chairs with small flower pots lining a sandy aisle, blue sky and headland behind"></div>
    <div class="brand">Vow Outfitters</div>
    <div class="contact">
      <p class="contact__name">Merel Thorpe</p>
      <p class="contact__line">0491 870 264</p>
      <p class="contact__line">vowoutfitters@mailbox-example.com</p>
      <p class="contact__line">www.vowoutfitters-example.com.au</p>
      <p class="contact__line">www.social-example.com/VowOutfitters</p>
    </div>
  </section>

  <section class="card card--back" aria-label="Business card back">
    <div class="photo photo--garden" role="img" aria-label="Photo of a harbourside garden ceremony: white chairs on a lawn either side of a white aisle runner, harbour bridge and city skyline behind"></div>
    <div class="band"></div>
    <div class="brand">Vow Outfitters</div>
  </section>

</main>
</body>
</html>
```